Brightmoor Partners Branding Revamp

We are a consulting company, looking for a way to display and promote our brand. We have 2 sides to the business- Brightmoor (financial) and Partners (cyber security). The financial side products relate to business necessities: card processing, website design/hosting/maintenance, VoIP phone systems. The cyber security side promotes a bundled package of 4 solutions: network vulnerability scan, dark web scan, anti-ransomeware/malware software, and image-level backups. We want people to understand that partnering with Brightmoor Partners gives them “Elevated Peace of Mind” (tagline). Current badge and logos uploaded.

Target Market(s)

Small businesses

Contact Information for Business Card

Lena Marwick, Vice President, lena@brightmoorpartners.example, 555-806-1937, www.brightmoorpartners.example

Requirements
Nice to have
• I do prefer the darker background for front and back

```html
<!DOCTYPE html>
<html lang="en">
<head>
<meta charset="utf-8">
<title>Brightmoor Partners — Business Card</title>
<link href="https://fonts.googleapis.com/css2?family=Exo+2:wght@700&family=Montserrat:wght@500&family=Roboto:wght@400&display=swap" rel="stylesheet">
<style>
  :root {
    --canvas-bg: #ffffff;
    --card-black: #050505;
    --brand-red: #c8141c;
    --deep-red: #8e0d12;
    --text-white: #ffffff;
    --shadow-grey: rgba(0, 0, 0, 0.35);
  }
  * { box-sizing: border-box; margin: 0; padding: 0; }
  html, body {
    width: 1200px;
    height: 1200px;
    overflow: hidden;
    background: var(--canvas-bg);
  }
  .canvas {
    position: relative;
    width: 1200px;
    height: 1200px;
  }
  .card {
    position: absolute;
    top: 450px;
    width: 520px;
    height: 300px;
    background: var(--card-black);
    box-shadow: 8px 8px 6px var(--shadow-grey);
    overflow: hidden;
  }
  .card--front { left: 60px; }
  .card--back { left: 620px; }

  /* Front */
  .front-brand {
    position: absolute;
    left: 0; right: 0;
    top: 110px;
    display: flex;
    flex-direction: column;
    align-items: center;
    gap: 22px;
  }
  .front-brand__mark {
    width: 26px;
    height: 26px;
    background: var(--brand-red);
  }
  .front-brand__name {
    font-family: "Montserrat", sans-serif;
    font-weight: 500;
    font-size: 22px;
    letter-spacing: 7px;
    color: var(--text-white);
    text-transform: uppercase;
  }

  /* Back */
  .back-header {
    position: absolute;
    left: 0; right: 0; top: 0;
    height: 102px;
    display: flex;
    align-items: center;
    padding-left: 44px;
    gap: 16px;
  }
  .back-header__mark {
    width: 52px;
    height: 52px;
    border: 4px solid var(--brand-red);
    border-radius: 50%;
  }
  .back-header__name {
    font-family: "Exo 2", sans-serif;
    font-weight: 700;
    font-size: 33px;
    letter-spacing: 1px;
    color: var(--text-white);
    text-transform: uppercase;
    line-height: 1;
  }
  .back-header__title {
    font-family: "Roboto", sans-serif;
    font-size: 12px;
    letter-spacing: 1px;
    color: var(--brand-red);
    text-transform: uppercase;
    margin-top: 4px;
  }
  .divider {
    position: absolute;
    left: 0; right: 0;
    top: 102px;
  }
  .divider__red { height: 5px; background: var(--deep-red); }
  .divider__white { height: 3px; background: var(--text-white); }

  .contact-list {
    position: absolute;
    left: 40px;
    top: 158px;
    list-style: none;
    display: flex;
    flex-direction: column;
    gap: 8px;
  }
  .contact-list__item {
    display: flex;
    align-items: center;
    gap: 14px;
    font-family: "Roboto", sans-serif;
    font-size: 24px;
    color: var(--text-white);
    line-height: 1.2;
  }
  .contact-icon { width: 22px; height: 22px; flex: none; }
</style>
</head>
<body>
<main class="canvas">

  <section class="card card--front" aria-label="Card front">
    <div class="front-brand">
      <span class="front-brand__mark"></span>
      <span class="front-brand__name">Brightmoor Partners</span>
    </div>
  </section>

  <section class="card card--back" aria-label="Card back">
    <header class="back-header">
      <span class="back-header__mark"></span>
      <div>
        <h1 class="back-header__name">Lena Marwick</h1>
        <p class="back-header__title">Vice President</p>
      </div>
    </header>
    <div class="divider">
      <div class="divider__red"></div>
      <div class="divider__white"></div>
    </div>

    <ul class="contact-list">
      <li class="contact-list__item">
        <svg class="contact-icon" viewBox="0 0 24 24" aria-hidden="true">
          <circle cx="12" cy="12" r="11" fill="#fff"/>
          <path d="M8.2 6.5l2 2.2-1 1.5c.8 1.6 2 2.8 3.6 3.6l1.5-1 2.2 2-.9 1.9c-4.6-.4-8.4-4.2-8.8-8.8z" fill="#050505"/>
        </svg>
        555-806-1937
      </li>
      <li class="contact-list__item">
        <svg class="contact-icon" viewBox="0 0 24 24" aria-hidden="true">
          <circle cx="12" cy="12" r="11" fill="#fff"/>
          <rect x="6" y="8" width="12" height="8.5" rx="1" fill="#050505"/>
          <path d="M6.5 8.6l5.5 4.2 5.5-4.2" stroke="#fff" stroke-width="1.2" fill="none"/>
        </svg>
        lena@brightmoorpartners.example
      </li>
      <li class="contact-list__item">
        <svg class="contact-icon" viewBox="0 0 24 24" aria-hidden="true">
          <circle cx="12" cy="12" r="11" fill="#fff"/>
          <g stroke="#050505" stroke-width="1.3" fill="none">
            <circle cx="12" cy="12" r="6.2"/>
            <ellipse cx="12" cy="12" rx="2.8" ry="6.2"/>
            <path d="M5.8 12h12.4M6.8 9h10.4M6.8 15h10.4"/>
          </g>
        </svg>
        www.brightmoorpartners.example
      </li>
    </ul>
  </section>

</main>
</body>
</html>
```